Gestaltung von Plakaten für Bereich der Qualitätssicherung
Zielgruppe
Wir sind Betreiber von zwei MERUFA Märkten.
Aufgabenstellung
Das Plakat dient zur internen Verwendung und soll anfallende Aufgaben im Bereich der Qualitätssicherung zeigen.
Es gibt die Marktleitung und 4 Abteilungen. In diesen 5 Bereichen fallen wiederkehrende Aufgaben in verschiedenen Zeitfenstern an.
Es soll herausstechen, dass die Marktleitung für die anderen 4 Abteilungen verantwortlich ist. (Organigramm)
Bitte fügen Sie zu jeden der 5 Zuständigkeitsbereiche eine freie Zeile hinzu. (Verantwortlich im Markt: __________)
Im Anhang habe ich eine Word Datei mit allen Abteilungen und deren Aufgaben und eine grobe Skizze hinzugefügt.
Überschrift des Plakats: Qualitätssicherung im Markt
Die Gestaltung soll einfach aber hochwertig wirken. Nicht verspielt. Weißer oder schlichter Hintergrund.
Das Ziel ist durch das Plakat eine Übersicht zu schaffen, wer für welche Aufgaben wann verantwortlich ist.
Wichtig ist das der Rhythmus (Wann muss es erledigt werden) am Plakat deutlich zu sehen ist.
Bitte fügen Sie das angehängte MERUFA Logo hinzu, dezent rechts unten im Eck.
In die Fußzeile bitte: BLT Abschlussprojekt von Jonas Kreibl, MERUFA Kreibl in Waldenbach
Wenn möglich bitte mit wenig kostenpflichtigen Stockmaterial.
Ich bin gespannt auf die Vorschläge.
Besten Dank im Voraus.

```html
<!DOCTYPE html>
<html lang="de">
<head>
<meta charset="utf-8">
<title>Qualitätssicherung im Markt</title>
<link href="https://fonts.googleapis.com/css2?family=Oswald:wght@700&family=Roboto+Condensed:wght@700&family=Lato:wght@400;700&display=swap" rel="stylesheet">
<style>
  :root{
    --paper:#ffffff;
    --frame:#707070;
    --ink:#111111;
    --navy:#1c2b4d;
    --yellow:#f7e237;
    --yellow-deep:#e7c514;
    --blue:#3a6bb3;
    --red:#c23a1a;
    --rule:#8a8a8a;
  }
  *{box-sizing:border-box;margin:0;padding:0}
  html,body{width:1200px;height:871px;overflow:hidden;background:var(--paper)}
  body{position:relative;font-family:"Lato",sans-serif;color:var(--ink)}
  .poster{position:absolute;left:52px;top:50px;width:1099px;height:778px;background:var(--frame);border:1px solid var(--ink)}
  .poster-title{position:absolute;left:0;right:0;top:14px;text-align:center;font-family:"Oswald",sans-serif;font-weight:700;font-size:68px;line-height:1;color:var(--paper);letter-spacing:4px;text-shadow:4px 4px 0 var(--navy);-webkit-text-stroke:1px var(--navy)}
  .stage{position:absolute;left:28px;top:106px;width:1043px;height:637px;background:var(--yellow)}
  .footer-note{position:absolute;right:26px;bottom:20px;font-size:10px;color:var(--paper);font-weight:400}
  .card{position:absolute;background:var(--paper);border:1.5px solid var(--ink);border-radius:12px;box-shadow:7px 7px 0 var(--yellow-deep)}
  .lead-card{left:100px;top:178px;width:997px;height:182px}
  .card-title{font-family:"Roboto Condensed",sans-serif;font-weight:700;color:var(--blue);font-size:24px;line-height:31px}
  .lead-card .card-title{position:absolute;left:14px;top:12px}
  .resp-label{font-size:12.5px;color:var(--ink)}
  .lead-card .resp-label{position:absolute;left:14px;top:53px}
  .resp-line{position:absolute;height:1px;background:var(--rule);width:196px}
  .lead-card .resp-line{left:16px;top:104px}
  .lead-icon{position:absolute;left:242px;top:38px;width:125px;height:110px}
  .duty-list{position:absolute;left:400px;top:16px;list-style:none}
  .duty-list li{display:flex;height:20.8px;font-weight:700;font-size:15.8px;line-height:20.8px}
  .rhythm{font-size:14.5px}
  .duty-list .rhythm{width:150px;color:var(--red)}
  .rhythm::before{content:"→ ";color:var(--ink)}
  .connectors{position:absolute;left:0;top:0;width:1200px;height:871px;pointer-events:none}
  .dept-card{top:406px;width:232px;padding:12px 14px}
  .dept-card .resp-label{margin-top:1px}
  .dept-card .resp-line{left:17px;top:122px}
  .task-list{list-style:none;margin-top:49px}
  .task-list li{margin-bottom:12px;font-weight:700;font-size:15.8px;line-height:20px}
  .task-list .rhythm{display:block;color:var(--red)}
  .dept-produce{left:100px;height:364px}
  .dept-dairy{left:355px;height:364px}
  .dept-frozen{left:610px;height:289px}
  .dept-grocery{left:865px;height:217px}
  .brand-mark{position:absolute;left:992px;top:738px;display:flex;flex-direction:row;align-items:center;gap:8px}
  .brand-square{width:14px;height:14px;background:var(--navy)}
  .brand-name{font-family:"Lato",sans-serif;font-weight:700;font-size:18px;color:var(--navy)}
</style>
</head>
<body>
  <div class="poster">
    <h1 class="poster-title">QUALITÄTSSICHERUNG IM MARKT</h1>
    <div class="stage"></div>
    <p class="footer-note">BLT Abschlussprojekt 2021 von Jonas Kreibl, MERUFA Kreibl in Waldenbach</p>
  </div>

  <section class="card lead-card">
    <h2 class="card-title">MARKTLEITUNG</h2>
    <p class="resp-label">Verantwortlich im Markt:</p>
    <div class="resp-line"></div>
    <svg class="lead-icon" viewBox="0 0 125 110" aria-hidden="true" fill="none" stroke="#6a6a6a" stroke-width="3" stroke-linecap="round">
      <circle cx="38" cy="60" r="32"/>
      <circle cx="38" cy="60" r="24"/>
      <line x1="38" y1="60" x2="38" y2="44"/>
      <circle cx="38" cy="62" r="3" fill="#6a6a6a"/>
      <rect x="30" y="18" width="16" height="6"/>
      <line x1="65" y1="8" x2="65" y2="108"/>
      <rect x="82" y="15" width="34" height="12" rx="6"/>
      <rect x="82" y="46" width="34" height="12" rx="6"/>
      <rect x="82" y="77" width="34" height="12" rx="6"/>
      <line x1="65" y1="21" x2="82" y2="21"/>
      <line x1="65" y1="52" x2="82" y2="52"/>
      <line x1="65" y1="83" x2="82" y2="83"/>
    </svg>
    <ul class="duty-list">
      <li><span class="rhythm">MONATLICH</span><span>Temperaturkontrolle aller Truhen</span></li>
      <li><span class="rhythm">1 × QUARTAL</span><span>Marktbegehung</span></li>
      <li><span class="rhythm">1 × JAHR</span><span>Hygieneschulung</span></li>
      <li><span class="rhythm">1 × JAHR</span><span>Mitarbeiterbelehrung Infektionsschutzgesetz</span></li>
      <li><span class="rhythm">NACH BEDARF</span><span>Dokumentation der Verantwortlichkeiten</span></li>
      <li><span class="rhythm">NACH BEDARF</span><span>Ablage Nachweisdokumente Schädlingsbekämpfung</span></li>
      <li><span class="rhythm">NACH BEDARF</span><span>Dokumentation und Ablage Warenrückruf</span></li>
    </ul>
  </section>

  <svg class="connectors" viewBox="0 0 1200 871" aria-hidden="true">
    <g fill="#e7c514">
      <polygon points="191,361 246,361 246,384 266,384 218,408 171,384 191,384"/>
      <polygon points="447,361 502,361 502,384 522,384 474,408 427,384 447,384"/>
      <polygon points="707,361 762,361 762,384 782,384 734,408 687,384 707,384"/>
      <polygon points="967,361 1022,361 1022,384 1042,384 994,408 947,384 967,384"/>
    </g>
    <g fill="#ffffff" stroke="#111111" stroke-width="1.5" stroke-linejoin="miter">
      <polygon points="185,359 240,359 240,378 260,378 212,402 165,378 185,378"/>
      <polygon points="441,359 496,359 496,378 516,378 468,402 421,378 441,378"/>
      <polygon points="701,359 756,359 756,378 776,378 728,402 681,378 701,378"/>
      <polygon points="961,359 1016,359 1016,378 1036,378 988,402 941,378 961,378"/>
    </g>
    <g fill="#ffffff">
      <rect x="186" y="356" width="53" height="4"/>
      <rect x="442" y="356" width="53" height="4"/>
      <rect x="702" y="356" width="53" height="4"/>
      <rect x="962" y="356" width="53" height="4"/>
    </g>
  </svg>

  <section class="card dept-card dept-produce">
    <h2 class="card-title">Abteilung<br>OBST und GEMÜSE</h2>
    <p class="resp-label">Verantwortlich im Markt:</p>
    <div class="resp-line"></div>
    <ul class="task-list">
      <li><span class="rhythm">TÄGLICH</span>Dokumentation Wareneingangskontrolle</li>
      <li><span class="rhythm">TÄGLICH</span>Temperaturkontrolle steckerfertige Truhen</li>
      <li><span class="rhythm">TÄGLICH</span>Kennzeichnung<br>„behandelte Ware“</li>
    </ul>
  </section>

  <section class="card dept-card dept-dairy">
    <h2 class="card-title">Abteilung<br>MOPRO</h2>
    <p class="resp-label">Verantwortlich im Markt:</p>
    <div class="resp-line"></div>
    <ul class="task-list">
      <li><span class="rhythm">TÄGLICH</span>Dokumentation Wareneingangskontrolle</li>
      <li><span class="rhythm">TÄGLICH</span>Temperaturkontrolle steckerfertige Truhen</li>
      <li><span class="rhythm">TÄGLICH</span>MHD-Qualitätskontrolle während der Lagerung</li>
    </ul>
  </section>

  <section class="card dept-card dept-frozen">
    <h2 class="card-title">Abteilung<br>TIEFKÜHL</h2>
    <p class="resp-label">Verantwortlich im Markt:</p>
    <div class="resp-line"></div>
    <ul class="task-list">
      <li><span class="rhythm">PRO LIEFERUNG</span>Dokumentation Wareneingangskontrolle</li>
      <li><span class="rhythm">WÖCHENTLICH</span>MHD-Qualitätskontrolle während der Lagerung</li>
    </ul>
  </section>

  <section class="card dept-card dept-grocery">
    <h2 class="card-title">Abteilung<br>LEBENSMITTEL</h2>
    <p class="resp-label">Verantwortlich im Markt:</p>
    <div class="resp-line"></div>
    <ul class="task-list">
      <li><span class="rhythm">WÖCHENTLICH</span>MHD-Qualitätskontrolle während der Lagerung</li>
    </ul>
  </section>

  <div class="brand-mark">
    <span class="brand-square"></span>
    <span class="brand-name">Merufa</span>
  </div>
</body>
</html>
```